Wirenexa

I'm looking to much improve our current website wirenexa.com
Updates

Low design quality

Target Market(s)

Commercial clients (Not-Residentials)

Industry/Entity Type

Office buildings and Industrial clients

Coding

Coded - Design and coding required

Number of Pages Required

5+ page

Requirements
Must have
• Very professional structured low voltage cabling projects for Wi-Fi, Audio/Video conference rooms, Access Control systems, CCTV.

```html
<!DOCTYPE html>
<html lang="en">
<head>
<meta charset="utf-8">
<title>Wirenexa — Professional Low Voltage Cabling</title>
<link href="https://fonts.googleapis.com/css2?family=Archivo:wght@400;500;600;700;800&family=Bebas+Neue&display=swap" rel="stylesheet">
<style>
:root{
  --red:#d8261c;
  --red-dark:#b81d15;
  --black:#0e0e0e;
  --dark:#161616;
  --dark-2:#1f1f1f;
  --band:#262626;
  --grey-box:#f2f2f2;
  --text:#1b1b1b;
  --muted:#555;
  --white:#fff;
}
*{box-sizing:border-box;margin:0;padding:0}
html,body{width:1200px;height:4399px;overflow:hidden}
body{font-family:"Archivo",Arial,sans-serif;color:var(--text);background:var(--white);position:relative}
.section{position:absolute;left:0;width:1200px}
.abs{position:absolute}
.accent{color:var(--red)}
.btn{position:absolute;background:var(--red);color:#fff;font-weight:700;font-size:12px;letter-spacing:.3px;display:flex;align-items:center;justify-content:center;text-transform:uppercase}
.h2{font-size:32px;font-weight:500;letter-spacing:-.3px}

/* hero */
.hero{top:0;height:632px;background:radial-gradient(ellipse at 30% 45%,#4a3424 0%,#2a1c16 30%,#121418 70%,#0b0b0d 100%)}
.hero-photo{position:absolute;inset:0;background:linear-gradient(100deg,rgba(190,90,40,.35) 0%,rgba(40,50,70,.25) 45%,rgba(10,10,12,.6) 75%)}
.logo{position:absolute;display:flex;align-items:center;gap:6px;font-family:"Bebas Neue",sans-serif;color:#fff}
.logo .sq{background:var(--red)}
.nav{position:absolute;top:38px;left:508px;display:flex;gap:34px;font-size:10px;color:#fff;font-weight:500}
.nav .on{color:var(--red)}
.call{position:absolute;left:972px;top:30px;color:#fff;font-size:11px;font-weight:600}
.call small{display:block;color:var(--red);font-size:8px;font-weight:500;margin-bottom:2px}
.side-dots{position:absolute;left:24px;top:276px;display:flex;flex-direction:column;align-items:center;gap:6px}
.side-dots i{width:3px;height:3px;border-radius:50%;background:#bbb;display:block}
.hero-title{position:absolute;left:626px;top:244px;width:470px;color:#fff;font-size:29px;font-weight:700;line-height:38px}
.hero-rule{position:absolute;left:626px;top:418px;width:430px;height:1px;background:rgba(255,255,255,.3)}
.hero-feats{position:absolute;left:626px;top:444px;display:flex;gap:22px;color:#fff;font-family:"Bebas Neue",sans-serif;font-size:17px;letter-spacing:.6px}
.hero-feats span{display:flex;align-items:center;gap:8px}

/* trust band */
.trust{top:632px;height:106px;background:var(--band);display:flex;align-items:center;padding-left:126px;gap:42px;color:#9b9b9b;font-weight:700;overflow:hidden;white-space:nowrap}
.trust .lbl{font-size:8px;font-weight:500;color:#888}
.trust .nm{font-size:14px;display:flex;align-items:center;gap:6px}
.trust .nm i{width:14px;height:14px;border-radius:50%;background:#8a8a8a;display:block}

/* about */
.about{top:738px;height:517px}
.about h2{position:absolute;left:126px;top:80px}
.about p{position:absolute;left:126px;top:138px;width:325px;font-size:11.5px;line-height:17.5px;color:#222}
.photo{position:absolute}

/* services */
.services{top:1255px;height:695px;background:radial-gradient(ellipse at 50% 40%,#3a3a3a 0%,#1d1d1d 55%,#0f0f0f 100%)}
.services h2{position:absolute;width:100%;text-align:center;top:100px;color:#fff}
.svc-card{position:absolute;top:172px;width:461px;height:345px;overflow:hidden}
.svc-tag{position:absolute;left:38px;top:240px;background:var(--red);color:#fff;font-size:11px;font-weight:700;padding:9px 18px}
.svc-desc{position:absolute;left:38px;top:283px;width:300px;color:#fff;font-size:11.5px;line-height:17px}
.arrow-btn{position:absolute;left:1046px;top:1573px}

/* expertise */
.expertise{top:1950px;height:597px}
.expertise h2{position:absolute;width:100%;text-align:center;top:100px}
.exp-box{position:absolute;width:297px;height:87px;background:var(--grey-box);display:flex;align-items:flex-end;justify-content:center;padding-bottom:26px;font-size:11.5px;font-weight:600}
.exp-ico{position:absolute;left:50%;top:-22px;margin-left:-22px}

/* key features */
.features{top:2547px;height:584px;background:radial-gradient(ellipse at 40% 50%,#2e2e2e 0%,#161616 60%,#0c0c0c 100%)}
.features h2{position:absolute;left:753px;top:112px;color:#fff}
.feat{position:absolute;left:750px;width:340px;display:flex;gap:14px}
.feat h3{color:var(--red);font-size:11.5px;font-weight:500;margin-bottom:3px}
.feat p{color:#ddd;font-size:11px;line-height:16.5px}

/* testimonials */
.testis{top:3131px;height:496px}
.testis h2{position:absolute;left:0;width:100%;top:90px;display:flex;justify-content:center;align-items:center;gap:16px}
.quote{position:absolute;top:170px;width:297px;background:var(--grey-box);padding:22px 20px;font-size:11.5px;line-height:18px;color:#222}
.who{position:absolute;top:297px;font-size:11.5px;line-height:18px;color:#222}
.dots{position:absolute;top:395px;left:578px;display:flex;gap:6px}
.dots i{width:4px;height:4px;border-radius:50%;background:#bbb;display:block}
.dots i:first-child{background:var(--red)}

/* cta + footer */
.dark-base{top:3755px;height:644px;background:var(--black)}
.cta-red{position:absolute;left:126px;top:3627px;width:432px;height:285px;background:var(--red);color:#fff;padding:48px 46px}
.cta-red h2{font-family:"Bebas Neue",sans-serif;font-weight:400;font-size:39px;line-height:44px;letter-spacing:.5px}
.cta-red h2 span{color:#1a1a1a}
.cta-red p{font-size:12.5px;margin-top:18px}
.cta-form{position:absolute;left:558px;top:3627px;width:516px;height:285px;background:var(--dark-2)}
.field{position:absolute;background:#0d0d0d;color:#ccc;font-size:11px;padding:12px 11px}
.send{position:absolute;left:45px;top:212px;width:208px;height:34px;background:var(--red);color:#fff;font-weight:700;font-size:11px;display:flex;align-items:center;justify-content:center}
.fcol{position:absolute;top:3992px;color:#ccc;font-size:10.5px;line-height:22px}
.fcol h4{font-size:10px;font-weight:500;color:#8d8d8d;margin-bottom:14px;text-transform:uppercase}
.fline{display:flex;gap:6px}
.badge{position:absolute;left:186px;top:4088px;width:84px;height:66px;border-radius:8px;background:linear-gradient(135deg,#6c3bb0,#d8261c,#e8a928,#2aa36d)}
.rule{position:absolute;left:126px;top:4262px;width:948px;height:1px;background:#2c2c2c}
.copy{position:absolute;left:126px;top:4288px;font-size:9px;color:#8d8d8d}
.social{position:absolute;left:982px;top:4284px;display:flex;gap:11px}
.social i{width:13px;height:13px;border-radius:50%;background:#fff;display:block}
</style>
</head>
<body>

<header class="section hero">
  <div class="hero-photo" role="img" aria-label="Photo of a technician working on a rack of orange and blue network cables"></div>
  <div class="logo" style="left:126px;top:26px;font-size:34px">
    <span class="sq" style="width:26px;height:26px;display:block"></span>Wirenexa
  </div>
  <nav class="nav">
    <span class="on">HOME</span><span>ABOUT US</span><span>SERVICES ⌄</span><span>KEY FEATURES</span><span>CONTACT</span>
  </nav>
  <div class="call"><small>CALL US TODAY</small>
    <svg width="9" height="9" viewBox="0 0 24 24" fill="#fff"><path d="M6.6 10.8a15 15 0 006.6 6.6l2.2-2.2c.3-.3.7-.4 1-.2 1.1.4 2.3.6 3.6.6.6 0 1 .4 1 1V20c0 .6-.4 1-1 1C10.6 21 3 13.4 3 4c0-.6.4-1 1-1h3.5c.6 0 1 .4 1 1 0 1.3.2 2.5.6 3.6.1.3 0 .7-.2 1z"/></svg>
    (800)-555-0147</div>
  <div class="side-dots">
    <span style="width:14px;height:18px;border:1.5px solid #ddd;border-radius:4px;display:block;margin-bottom:10px"></span>
    <span style="width:8px;height:8px;border-radius:50%;border:1.5px solid #ddd;display:block"></span>
    <i></i><i></i><i></i>
  </div>
  <h1 class="hero-title">Professional Cabling for Computers, Security Cameras, Wi-Fi, VOIP Phones, Access Control, Video and Audio.</h1>
  <div class="hero-rule"></div>
  <div class="hero-feats">
    <span><svg width="16" height="16" viewBox="0 0 24 24" fill="none" stroke="#fff" stroke-width="2"><path d="M12 3l8 3v6c0 5-4 8-8 9-4-1-8-4-8-9V6z"/><path d="M8 12l3 3 5-5"/></svg>SAFE &amp; SECURE</span>
    <span><svg width="16" height="16" viewBox="0 0 24 24" fill="none" stroke="#fff" stroke-width="2"><circle cx="12" cy="12" r="9"/><path d="M12 7v5l3 2"/></svg>24X7 SUPPORT</span>
    <span><svg width="16" height="16" viewBox="0 0 24 24" fill="none" stroke="#fff" stroke-width="2"><circle cx="12" cy="12" r="9"/><path d="M12 7v10M9 9.5h4.5a1.8 1.8 0 010 3.5h-3a1.8 1.8 0 000 3.5H15"/></svg>LOW COST</span>
  </div>
</header>

<section class="section trust">
  <span class="lbl">TRUSTED BY</span>
  <span class="nm"><i></i>Northfield Council</span>
  <span class="nm">Ridgeway Power</span>
  <span class="nm">Harbor City</span>
  <span class="nm">Dunmore</span>
  <span class="nm"><i></i>Bayline Port</span>
  <span class="nm">Stanfeld</span>
  <span class="nm"><i></i>cyclesource</span>
  <span class="nm">Borvale</span>
</section>

<section class="section about">
  <h2 class="h2"><span class="accent">About</span> Wirenexa</h2>
  <p>Wirenexa is your premier provider of professional low voltage cabling services in Virginia, Washington DC, and Maryland. With a focus on quality, reliability, and attention to detail, we deliver exceptional cabling solutions for audio, video, security systems, computer networks, and more.</p>
  <div class="btn" style="left:126px;top:264px;width:154px;height:36px">MORE ABOUT US</div>
  <div class="photo" style="left:550px;top:76px;width:440px;height:314px;background:linear-gradient(135deg,#1d3a5a,#8a2a3a 55%,#1a2030)" role="img" aria-label="Photo of a technician in a red hard hat and safety glasses routing cables"></div>
  <div class="photo" style="left:833px;top:247px;width:240px;height:176px;background:linear-gradient(160deg,#1b3f8a,#c43a3a 60%,#2a1a1a);border:1px solid #fff" role="img" aria-label="Photo of a bundle of network cables being terminated"></div>
</section>

<section class="section services">
  <h2 class="h2"><span class="accent">Our</span> Services</h2>
  <div class="svc-card" style="left:126px;background:linear-gradient(135deg,#c2601f,#2d4a6a 50%,#1a1a1a)" role="img" aria-label="Photo of a technician working among colorful cables in an office server room">
    <div class="svc-tag">COMMERCIAL SERVICES</div>
    <p class="svc-desc">Complete office low voltage cabling and Wi-Fi for your network and security system.</p>
  </div>
  <div class="svc-card" style="left:613px;background:linear-gradient(135deg,#d8541e,#1f4d9a 55%,#101a2a)" role="img" aria-label="Photo of a technician in a blue hard hat beside an illuminated patch panel">
    <div class="svc-tag">INDUSTRIAL SERVICES</div>
    <p class="svc-desc">Structured cabling, IDF and MDF for warehouses, manufacturing facilities and others.</p>
  </div>
  <div class="btn" style="left:514px;top:565px;width:172px;height:34px">VIEW ALL SERVICES</div>
</section>
<svg class="arrow-btn" width="56" height="56" viewBox="0 0 56 56"><rect x="28" y="0" width="39.6" height="39.6" transform="rotate(45 28 0)" fill="#d8261c"/><path d="M20 28h16M30 22l6 6-6 6" stroke="#fff" stroke-width="2.4" fill="none"/></svg>

<section class="section expertise">
  <h2 class="h2"><span class="accent">Wirenexa</span> Expertise</h2>
  <div class="exp-box" style="left:126px;top:194px">Voice &amp; Data Cable Installations
    <svg class="exp-ico" width="44" height="44" viewBox="0 0 44 44"><circle cx="22" cy="22" r="20" fill="#d8261c"/><path d="M17 14v16M27 14v16M15 18h4M25 18h4" stroke="#fff" stroke-width="2"/></svg></div>
  <div class="exp-box" style="left:452px;top:194px">Copper Cable CAT6 and CAT7
    <svg class="exp-ico" width="44" height="44" viewBox="0 0 44 44"><circle cx="22" cy="22" r="20" fill="#d8261c"/><rect x="15" y="14" width="14" height="16" rx="2" fill="none" stroke="#fff" stroke-width="2"/><path d="M19 18v8M22 18v8M25 18v8" stroke="#fff" stroke-width="1.6"/></svg></div>
  <div class="exp-box" style="left:777px;top:194px">Fiber Cable Single &amp; Multi Mode
    <svg class="exp-ico" width="44" height="44" viewBox="0 0 44 44"><circle cx="22" cy="22" r="20" fill="#d8261c"/><path d="M13 27c6-1 10-6 18-12M14 22c6 0 10-4 16-8M16 30c5-3 9-6 16-8" stroke="#fff" stroke-width="1.8" fill="none"/></svg></div>
  <div class="exp-box" style="left:126px;top:332px">Conduit Installations
    <svg class="exp-ico" width="44" height="44" viewBox="0 0 44 44"><circle cx="22" cy="22" r="20" fill="#d8261c"/><circle cx="22" cy="23" r="7" fill="none" stroke="#fff" stroke-width="2"/><path d="M18 13v4M26 13v4" stroke="#fff" stroke-width="2"/></svg></div>
  <div class="exp-box" style="left:452px;top:332px">IDF and MDF Installations
    <svg class="exp-ico" width="44" height="44" viewBox="0 0 44 44"><circle cx="22" cy="22" r="20" fill="#d8261c"/><path d="M16 14v16M22 14v16M28 14v16" stroke="#fff" stroke-width="2.4"/></svg></div>
  <div class="exp-box" style="left:777px;top:332px">Voltrix VX-8000 Certification
    <svg class="exp-ico" width="44" height="44" viewBox="0 0 44 44"><circle cx="22" cy="22" r="20" fill="#d8261c"/><rect x="14" y="14" width="16" height="16" rx="2" fill="none" stroke="#fff" stroke-width="2"/><path d="M18 22l3 3 5-6" stroke="#fff" stroke-width="2" fill="none"/></svg></div>
  <div class="btn" style="left:517px;top:465px;width:166px;height:38px">REQUEST A QUOTE</div>
</section>

<section class="section features">
  <div class="abs" style="left:126px;top:95px;width:182px;height:330px;background:var(--red)"></div>
  <div class="abs" style="left:140px;top:109px;width:372px;height:314px;background:linear-gradient(120deg,#3a2a22,#a8302a 55%,#1c1c1c)" role="img" aria-label="Photo of a technician wearing glasses organizing red network cables at a patch panel"></div>
  <div class="abs" style="left:423px;top:309px;width:239px;height:176px;background:linear-gradient(150deg,#1f4fa0,#6fa3d8 50%,#15233a)" role="img" aria-label="Photo of hands plugging blue patch cables into a switch"></div>
  <h2 class="h2"><span class="accent">Key</span> Features</h2>
  <div class="feat" style="top:172px"><svg width="44" height="44" viewBox="0 0 44 44" style="flex:none"><circle cx="22" cy="22" r="20" fill="#d8261c"/><circle cx="22" cy="19" r="5" fill="none" stroke="#fff" stroke-width="2"/><path d="M14 31c2-4 14-4 16 0" stroke="#fff" stroke-width="2" fill="none"/></svg><div><h3>Expertise and Experience</h3><p>With years of experience in the industry, we bring a wealth of expertise to every project.</p></div></div>
  <div class="feat" style="top:239px"><svg width="44" height="44" viewBox="0 0 44 44" style="flex:none"><circle cx="22" cy="22" r="20" fill="#d8261c"/><path d="M16 14v16M22 14v16M28 14v16" stroke="#fff" stroke-width="2.4"/></svg><div><h3>Comprehensive Solutions</h3><p>From copper CAT6 and CAT7 cabling to fiber optic installations, we offer them all.</p></div></div>
  <div class="feat" style="top:305px"><svg width="44" height="44" viewBox="0 0 44 44" style="flex:none"><circle cx="22" cy="22" r="20" fill="#d8261c"/><circle cx="22" cy="22" r="8" fill="none" stroke="#fff" stroke-width="2"/><path d="M18 22l3 3 5-6" stroke="#fff" stroke-width="2" fill="none"/></svg><div><h3>Quality Workmanship</h3><p>At Wirenexa, we take pride in our work and strive for excellence in all project we undertake.</p></div></div>
  <div class="feat" style="top:372px"><svg width="44" height="44" viewBox="0 0 44 44" style="flex:none"><circle cx="22" cy="22" r="20" fill="#d8261c"/><path d="M14 30V16h8v14M22 30V12h8v18M12 30h20" stroke="#fff" stroke-width="2" fill="none"/></svg><div><h3>Commercial and Industrial</h3><p>From office buildings to data centers, we have the capabilities to handle diverse requirements.</p></div></div>
  <div class="feat" style="top:439px"><svg width="44" height="44" viewBox="0 0 44 44" style="flex:none"><circle cx="22" cy="22" r="20" fill="#d8261c"/><circle cx="18" cy="18" r="3.5" fill="#fff"/><circle cx="27" cy="18" r="3.5" fill="#fff"/><path d="M12 29c1-5 11-5 12 0M20 29c1-5 11-5 12 0" stroke="#fff" stroke-width="2" fill="none"/></svg><div><h3>Customer Satisfaction</h3><p>Our commitment to customer satisfaction drives everything we do.</p></div></div>
</section>

<section class="section testis">
  <h2 class="h2"><svg width="64" height="46" viewBox="0 0 64 46"><path d="M2 24C2 10 10 2 22 0v8c-6 2-9 6-9 12h9v24H2zM36 24C36 10 44 2 56 0v8c-6 2-9 6-9 12h9v24H36z" fill="#d8261c"/></svg><span><span class="accent">Client</span> Testimonials</span></h2>
  <div class="quote" style="left:126px;height:88px">"There were zero items identified at the audit, and no further action is required."</div>
  <div class="who" style="left:146px">Contract Manager,<br>Government Client</div>
  <div class="quote" style="left:448px;height:106px">"The site came up extremely well for the event and I was very pleased with the outcome."</div>
  <div class="who" style="left:468px;top:315px">Maintenance Contract Supervisor,<br>Government Client</div>
  <div class="quote" style="left:770px;height:88px">"Management of subcontractors on a remote site was above the expected standard."</div>
  <div class="who" style="left:790px">Superintendent's Representative,<br>Government Client</div>
  <div class="dots"><i></i><i></i><i></i><i></i><i></i></div>
</section>

<footer class="section dark-base"></footer>
<div class="cta-red">
  <h2>ENGAGE WITH <span>WIRENEXA</span><br>&amp; REQUEST A CALLBACK</h2>
  <p>Submit the form and we will contact you within 1 hour.</p>
</div>
<form class="cta-form">
  <div class="field" style="left:45px;top:36px;width:208px;height:38px">First Name</div>
  <div class="field" style="left:263px;top:36px;width:208px;height:38px">Last Name</div>
  <div class="field" style="left:45px;top:83px;width:208px;height:38px">Email</div>
  <div class="field" style="left:263px;top:83px;width:208px;height:38px">Phone</div>
  <div class="field" style="left:45px;top:131px;width:426px;height:72px">Message</div>
  <div class="send">SEND</div>
</form>

<div class="logo" style="left:126px;top:3988px;font-size:40px">
  <span class="sq" style="width:32px;height:32px;display:block"></span>Wirenexa
</div>
<div class="badge" role="img" aria-label="Anniversary badge"></div>

<div class="fcol" style="left:415px"><h4>Navigation</h4>Home<br>About Us<br>Services<br>Key Features<br>Contact</div>
<div class="fcol" style="left:567px"><h4>Services</h4>Commercial<br>Industrial<br>Residential</div>
<div class="fcol" style="left:712px"><h4>Main Office - VA</h4>
  <div class="fline"><span>⌖</span><span>4410 Meridian Ave<br>Suite 250<br>Fairfax, VA 22030</span></div>
  <div class="fline" style="margin-top:20px"><span>✆</span><span>(800) 555-0147 (National)<br>(571) 555-0193 (Local)</span></div>
  <div class="fline" style="margin-top:20px"><span>✉</span><span>sales@wirenexa.com</span></div>
</div>
<div class="fcol" style="left:942px"><h4>Regional Office - MD</h4>
  <div class="fline"><span>⌖</span><span>2150 Harbor Lane<br>Suite 400<br>Rockville, MD, 20850</span></div>
</div>
<div class="rule"></div>
<div class="copy">COPYRIGHT © 2025 WIRENEXA. ALL RIGHTS RESERVED.</div>
<div class="social"><i></i><i></i><i></i><i></i></div>

</body>
</html>
```